Bref créative
VerdaLune
Business Cards etc...
Professional
Carmen Delvoe
Owner
3284-B Willow Crest Rd. #261
Greensboro, NC 27490
verdalunenc@mailbox.example
www.VerdaLuneNC.example
Landscape Management Services
Striving for earth friendly services
Member of 2% Pour Le Sol, Has a logo
landscaping | hardscapes | lighting | irrigation | water features | design | walls | patios | contract lawncare |

```html
<!DOCTYPE html>
<html lang="en">
<head>
<meta charset="UTF-8">
<title>VerdaLune — Business Card</title>
<link rel="stylesheet" href="https://fonts.googleapis.com/css2?family=PT+Sans:wght@400;700&display=swap">
<style>
  :root {
    --page: #eee9e1;
    --card: #ffffff;
    --forest: #3e6b35;
    --leaf: #7fb13d;
    --ink: #3a3a3a;
    --muted: #666666;
    --rule: #9a9a9a;
  }
  * { margin: 0; padding: 0; box-sizing: border-box; }
  html, body {
    width: 1200px; height: 965px; overflow: hidden;
    background: var(--page);
  }
  .card {
    position: absolute; left: 80px; top: 187px;
    width: 1040px; height: 590px;
    background: var(--card);
    border-radius: 40px;
    overflow: hidden;
    box-shadow: 0 6px 18px rgba(0,0,0,0.18);
    font-family: "PT Sans", Arial, sans-serif;
  }
  .band { position: absolute; top: 0; bottom: 0; width: 62px; background: var(--forest); }
  .band--left { left: 0; }
  .band--right { right: 0; }
  .band-line { position: absolute; top: 0; bottom: 0; width: 4px; background: var(--forest); }
  .band-line--left { left: 72px; }
  .band-line--right { right: 72px; }

  .brand { position: absolute; left: 120px; top: 90px; display: flex; align-items: center; }
  .brand-dot {
    width: 120px; height: 120px; border-radius: 50%;
    background: var(--leaf); margin-right: 36px; flex: none;
  }
  .brand-name {
    font-family: "PT Sans", Arial, sans-serif; font-weight: 700;
    font-size: 118px; line-height: 1; color: var(--forest);
  }

  .person { position: absolute; left: 172px; top: 350px; }
  .person-name { font-size: 40px; font-weight: 700; color: var(--forest); line-height: 1.1; }
  .person-role { font-size: 26px; color: var(--muted); margin-top: 2px; }

  .divider { position: absolute; left: 490px; top: 318px; width: 2px; height: 176px; background: var(--rule); }

  .contact { position: absolute; left: 520px; top: 320px; list-style: none; color: var(--ink); font-size: 27px; line-height: 1.3; }
  .contact li { display: flex; align-items: center; }
  .contact .address { padding-left: 40px; margin-bottom: 6px; }
  .contact svg { width: 26px; height: 26px; margin-right: 14px; flex: none; }
  .contact li + li { margin-top: 4px; }
</style>
</head>
<body>
  <section class="card" aria-label="VerdaLune business card">
    <div class="band band--left"></div>
    <div class="band-line band-line--left"></div>
    <div class="band band--right"></div>
    <div class="band-line band-line--right"></div>

    <div class="brand">
      <span class="brand-dot"></span>
      <span class="brand-name">VerdaLune</span>
    </div>

    <div class="person">
      <p class="person-name">Carmen Delvoe</p>
      <p class="person-role">Owner</p>
    </div>

    <div class="divider"></div>

    <ul class="contact">
      <li class="address">3284-B Willow Crest Rd. #261<br>Greensboro, NC 27490</li>
      <li>
        <svg viewBox="0 0 24 24" aria-hidden="true"><path fill="#3e6b35" d="M6.6 10.8c1.4 2.8 3.8 5.1 6.6 6.6l2.2-2.2c.3-.3.7-.4 1-.2 1.1.4 2.3.6 3.6.6.6 0 1 .4 1 1V20c0 .6-.4 1-1 1C10.6 21 3 13.4 3 4c0-.6.4-1 1-1h3.5c.6 0 1 .4 1 1 0 1.3.2 2.5.6 3.6.1.3 0 .7-.2 1z"/></svg>
        336-555-0184
      </li>
      <li>
        <svg viewBox="0 0 24 24" aria-hidden="true"><text x="12" y="19" text-anchor="middle" font-family="PT Sans, Arial, sans-serif" font-weight="700" font-size="22" fill="#3a3a3a">@</text></svg>
        verdalunenc@mailbox.example
      </li>
      <li>
        <svg viewBox="0 0 24 24" aria-hidden="true"><g fill="none" stroke="#555" stroke-width="1.8"><circle cx="12" cy="12" r="9"/><ellipse cx="12" cy="12" rx="4" ry="9"/><path d="M3 12h18M5 7h14M5 17h14"/></g></svg>
        www.VerdaLuneNC.example
      </li>
    </ul>
  </section>
</body>
</html>
```